Business cards and logo for kitchen and bath remodeling company

We want an elegant card but that calls attention something unique and when people see it they remember us. A log that we can use for our own. We are a kitchen and bathroom remodeling company. We are 3 partners staring the company we are located in seattle washington usa. We try to give the best experience and luxury look in our projects and we are looking to show that in our cards. I added a sample of a card I really like. I like the black and gold look but gray blue or green in a metallic look would look nice. I'm open to any color.

Target Market(s)

Home owners.

Industry/Entity Type

Construction

Contact Information for Business Card

Larchmont and Vey builders

Colors

Designer to choose colors to be used in the design.

Requirements
Must have
• Make a Logo
• Logo to be unique
• Name of company larchmont and vey builders
Nice to have
• Have a good color scheme
• Front design to connect with back of card

```html
<!DOCTYPE html>
<html lang="en">
<head>
<meta charset="utf-8">
<title>Larchmont and Vey Builders – Business Cards</title>
<link rel="stylesheet" href="https://fonts.googleapis.com/css2?family=Cinzel:wght@500;600;700&display=swap">
<style>
  :root {
    --page-bg: #d9d9d9;
    --card-black: #0c0d0f;
    --card-charcoal: #1b1d20;
    --gold: #c9a25a;
    --gold-light: #ecd08e;
    --gold-deep: #8a6a2e;
  }
  * { box-sizing: border-box; margin: 0; padding: 0; }
  html, body {
    width: 1200px;
    height: 1200px;
    overflow: hidden;
  }
  body {
    background: var(--page-bg);
    font-family: "Cinzel", serif;
    position: relative;
  }
  .card {
    position: absolute;
    left: 150px;
    width: 900px;
    height: 514px;
    background: radial-gradient(ellipse at 45% 35%, var(--card-charcoal) 0%, var(--card-black) 75%);
    color: var(--gold);
  }
  .card--front { top: 70px; }
  .card--back { top: 616px; }

  .wordmark {
    position: absolute;
    left: 0;
    right: 0;
    text-align: center;
    font-weight: 600;
    color: var(--gold);
    letter-spacing: 0.04em;
    text-transform: uppercase;
    line-height: 1.1;
  }
  .card--front .wordmark {
    top: 200px;
    font-size: 40px;
  }
  .card--back .wordmark {
    top: 225px;
    font-size: 46px;
  }

  .divider {
    position: absolute;
    left: 90px;
    top: 330px;
    width: 720px;
    height: 4px;
  }

  .person {
    position: absolute;
    left: 148px;
    top: 405px;
  }
  .person__name {
    font-size: 32px;
    font-weight: 600;
    color: var(--gold-light);
    letter-spacing: 0.01em;
  }
  .person__title {
    font-size: 14px;
    font-weight: 600;
    margin-top: 6px;
    margin-left: 5px;
  }

  .contact {
    position: absolute;
    left: 570px;
    top: 400px;
    list-style: none;
    font-size: 13px;
    font-weight: 600;
    color: var(--gold-light);
  }
  .contact li {
    position: relative;
    padding-left: 20px;
    line-height: 19px;
  }
  .contact li::before {
    content: "";
    position: absolute;
    left: 0;
    top: 7px;
    width: 4px;
    height: 4px;
    border-radius: 50%;
    background: var(--gold-light);
  }
</style>
</head>
<body>
  <section class="card card--front">
    <h1 class="wordmark">Larchmont and Vey Builders</h1>

    <svg class="divider" viewBox="0 0 720 4" aria-hidden="true">
      <defs>
        <linearGradient id="divider-gold" x1="0" x2="1" y1="0" y2="0">
          <stop offset="0" stop-color="#c9a25a" stop-opacity="0"/>
          <stop offset="0.35" stop-color="#8a6a2e"/>
          <stop offset="0.5" stop-color="#ecd08e"/>
          <stop offset="0.85" stop-color="#c9a25a"/>
          <stop offset="1" stop-color="#c9a25a" stop-opacity="0"/>
        </linearGradient>
      </defs>
      <rect x="0" y="1" width="720" height="2" fill="url(#divider-gold)"/>
    </svg>

    <div class="person">
      <p class="person__name">Your Name</p>
      <p class="person__title">Designation</p>
    </div>

    <ul class="contact">
      <li>Your Address Here</li>
      <li>000-0000-00</li>
      <li>youremail@mail.com</li>
      <li>Social Media</li>
    </ul>
  </section>

  <section class="card card--back">
    <p class="wordmark">Larchmont and Vey Builders</p>
  </section>
</body>
</html>
```